Velmora Partners Logo and Business Card Design

We already have the rough logo shape (however please make the lines on the logo much thicker so a dark background is not required to see it) . see photos uploaded.
It needs to be refined with color and digitized and then have a front and back business card layout done.
The services are high vibration healing support through a therapy and feng shui service offering. We want people to Feel Happiness, Feel Prosperity and Feel Peace. (the back of the card would have these phrases on it) So a warm, calm and peaceful feeling card.
We would like the card to use the logo provided (with thicker lines and color added) but below the graphic please use the name "Velmora Partners" NOT Velmora.
We also would like to use the colors in the colorized matrix shown in photos (gold and purple) but on the lighter side. Thanks for your time!

Front of Card should include: Logo, with Company Name: Velmora Partners as part of logo, Name: Dara Pemberton email: dara@velmora-example.me web: www.velmora-example.me mobile: 555.218.4096 at bottom of front list Family Constellation | Feng Shui

Back of Card should have the logo and the following listed vertically:

PERSONAL | BUSINESS (Larger size then smaller bullet items below)
*Find Happiness
*Find Prosperity
*Find Peace

Target Market(s)

Target market is both business and personal

Contact Information for Business Card

Front of Card should include: Logo, with Company Name: Velmora Partners as part of logo, Name: Dara Pemberton email: dara@velmora-example.me web: www.velmora-example.me mobile: 555.218.4096 at bottom of front list Family Constellation | Feng Shui ++++ Back of Card should have the logo and the following listed vertically: PERSONAL | BUSINESS (Larger size then smaller bullet items below) *Find Happiness *Find Prosperity *Find Peace

Font styles to use
Sans Serif

Colors

Designer to choose colors to be used in the design.

Requirements
Nice to have
• Nice light contrast color for the back of card background
Should not have
• No dark colored background on Card.

```html
<!DOCTYPE html>
<html lang="en">
<head>
<meta charset="utf-8">
<title>Velmora Partners – Business Card</title>
<link rel="stylesheet" href="https://fonts.googleapis.com/css2?family=Jost:wght@400;500;600;700&display=swap">
<style>
  :root {
    --backdrop: #b2aa9a;
    --card-light: #eadcf4;
    --card-back: #f6efdc;
    --card-back-edge: #efe4c6;
    --ink-purple: #45177f;
    --accent-gold: #e0c21a;
    --accent-gold-deep: #a8870a;
  }
  * { margin: 0; padding: 0; box-sizing: border-box; }
  html, body {
    width: 1200px;
    height: 2400px;
    overflow: hidden;
    background: var(--backdrop);
    font-family: "Jost", "Futura", sans-serif;
  }
  .canvas {
    position: relative;
    width: 1200px;
    height: 2400px;
  }
  .card {
    position: absolute;
    left: 88px;
    width: 1025px;
    height: 639px;
    line-height: 1;
    color: var(--ink-purple);
  }
  .card--front { top: 133px; background: var(--card-light); }
  .card--back {
    top: 903px;
    background: linear-gradient(110deg, var(--card-back) 0%, var(--card-back) 55%, var(--card-back-edge) 100%);
  }
  .card > * { position: absolute; white-space: nowrap; }

  .brand { display: flex; align-items: center; gap: 12px; font-weight: 600; }
  .brand-dot { display: block; border-radius: 50%; border: 4px solid var(--accent-gold); }

  .card--front .brand { left: 38px; top: 232px; font-size: 36px; }
  .card--front .brand-dot { width: 30px; height: 30px; }
  .card--front .website { right: 40px; top: 37px; font-size: 24px; font-weight: 500; }
  .card--front .person-name { right: 40px; top: 300px; font-size: 76px; font-weight: 700; letter-spacing: -0.5px; }
  .card--front .email { right: 40px; top: 536px; font-size: 25px; font-weight: 500; }
  .card--front .mobile { right: 40px; top: 573px; font-size: 28px; font-weight: 500; }
  .card--front .services { left: 38px; top: 575px; font-size: 25px; font-weight: 400; }

  .card--back .brand { left: 0; right: 0; justify-content: center; top: 320px; font-size: 44px; }
  .card--back .brand-dot { width: 38px; height: 38px; }
  .card--back .audience { left: 0; right: 0; text-align: center; top: 440px; font-size: 30px; font-weight: 400; }
  .card--back .promise-list {
    left: 0; right: 0; top: 492px;
    list-style: none;
    text-align: center;
    font-size: 20px;
    font-weight: 500;
    line-height: 32px;
    color: var(--accent-gold-deep);
  }
</style>
</head>
<body>
<main class="canvas">
  <section class="card card--front" aria-label="Card front">
    <div class="brand"><span class="brand-dot"></span><span class="brand-name">Velmora Partners</span></div>
    <p class="website">www.velmora-example.me</p>
    <h1 class="person-name">Dara Pemberton</h1>
    <p class="email">email: dara@velmora-example.me</p>
    <p class="mobile">mobile: 555.218.4096</p>
    <p class="services">FAMILY CONSTELLATION | FENG SHUI</p>
  </section>

  <section class="card card--back" aria-label="Card back">
    <div class="brand"><span class="brand-dot"></span><span class="brand-name">Velmora Partners</span></div>
    <p class="audience">PERSONAL | BUSINESS</p>
    <ul class="promise-list">
      <li>FIND HAPPINESS</li>
      <li>FIND PROSPERITY</li>
      <li>FIND PEACE</li>
    </ul>
  </section>
</main>
</body>
</html>
```